New company branded Power Point Template for presentations

We would like to have a clean and professional PowerPoint template made for our rebranding effort. It will be for our main company (Gordavexa) and will be used for both general introductory presentations and more technical industry related webinar and in-person presentations. We are a company in the manufacturing space working primarily in automotive. We provide simulation services to optimize production and softwares to allow users to do the same for themselves. The template needs to be easy to modify (even for novice users). I would like a good cover slide, content slides with common title / logo / etc. and a Q&A slide along with a final slide "Thank you" of similar. I have included our brand style guide in a high res pdf. Its images should be sufficient but please let me know if that is not the case.

```html
<!DOCTYPE html>
<html lang="en">
<head>
<meta charset="utf-8">
<title>Gordavexa – Any Questions</title>
<link href="https://fonts.googleapis.com/css2?family=Montserrat:ital,wght@0,400;0,500;0,700;0,800;1,400&display=swap" rel="stylesheet">
<style>
  :root {
    --stage: #00355a;
    --slide: #f6f7f7;
    --teal: #0d96ad;
    --amber: #eaa800;
    --ink: #383838;
    --muted: #4a4a4a;
  }
  * { margin: 0; padding: 0; box-sizing: border-box; }
  html, body { width: 1200px; height: 1001px; overflow: hidden; }
  body {
    background: var(--stage);
    font-family: "Montserrat", Arial, sans-serif;
    position: relative;
  }
  .slide {
    position: absolute;
    left: 0; top: 163px;
    width: 1200px; height: 675px;
    background: var(--slide);
    overflow: hidden;
  }
  .brand {
    position: absolute;
    right: 82px; top: 80px;
    display: flex; align-items: center; gap: 8px;
    font-weight: 800; font-size: 20px; color: var(--teal);
  }
  .brand-square { width: 14px; height: 14px; background: var(--amber); }
  .title {
    position: absolute; left: 0; right: 0; top: 103px;
    text-align: center;
    font-weight: 800; font-size: 48px; letter-spacing: 1px;
    color: var(--teal); line-height: 1.1;
  }
  .subtitle {
    position: absolute; left: 0; right: 0; top: 167px;
    text-align: center;
    font-style: italic; font-size: 17px;
    color: var(--amber);
  }
  .faq-icon {
    position: absolute;
    width: 101px; height: 101px;
    background: var(--amber);
    display: flex; align-items: center; justify-content: center;
  }
  .faq-icon svg { width: 64px; height: 64px; }
  .faq-text { position: absolute; width: 385px; }
  .faq-heading {
    font-weight: 700; font-size: 21px; letter-spacing: 0.4px;
    color: var(--teal); line-height: 1; margin-bottom: 10px;
    white-space: nowrap;
  }
  .faq-body {
    font-size: 12.6px; line-height: 18.3px; letter-spacing: -0.25px;
    color: var(--ink); text-align: left;
  }
  .closing-heading {
    position: absolute; left: 0; right: 0; top: 541px;
    text-align: center;
    font-weight: 700; font-size: 27.5px; color: var(--teal);
  }
  .closing-note {
    position: absolute; left: 0; right: 0; top: 584px;
    text-align: center;
    font-style: italic; font-size: 16.5px; color: var(--muted);
  }
</style>
</head>
<body>
  <main class="slide">
    <div class="brand"><span class="brand-square"></span>Gordavexa</div>

    <h1 class="title">ANY QUESTIONS?</h1>
    <p class="subtitle">We're here to clarify and support your success.</p>

    <div class="faq-icon" style="left:109px; top:224px;">
      <svg viewBox="0 0 64 64" fill="none" stroke="#fff" stroke-width="3" stroke-linejoin="round" aria-hidden="true">
        <path d="M28 6h8l1.5 7 5 2.5 6-4 5.5 5.5-4 6 2.5 5 7 1.5v8l-7 1.5-2.5 5 4 6-5.5 5.5-6-4-5 2.5L36 58h-8l-1.5-7-5-2.5-6 4-5.5-5.5 4-6-2.5-5L4 36v-8l7-1.5 2.5-5-4-6L15 10l6 4 5-2.5z"/>
        <circle cx="32" cy="32" r="11"/>
        <circle cx="32" cy="32" r="5"/>
      </svg>
    </div>
    <div class="faq-text" style="left:225px; top:227px;">
      <h2 class="faq-heading">INDUSTRIES WE SERVE</h2>
      <p class="faq-body">Our simulation and optimization tools are especially valuable for the automotive, aerospace, and industrial manufacturing sectors. These industries demand high precision, efficiency, and speed—exactly what our technology delivers.</p>
    </div>

    <div class="faq-icon" style="left:629px; top:224px;">
      <svg viewBox="0 0 64 64" fill="none" stroke="#fff" stroke-width="2.5" stroke-linecap="round" aria-hidden="true">
        <path d="M12 34v-6a20 20 0 0 1 40 0v6"/>
        <rect x="8" y="32" width="8" height="16" rx="3"/>
        <rect x="48" y="32" width="8" height="16" rx="3"/>
        <path d="M12 48c0 6 6 8 14 8"/>
        <rect x="26" y="53" width="8" height="5" rx="1.5"/>
      </svg>
    </div>
    <div class="faq-text" style="left:745px; top:227px;">
      <h2 class="faq-heading">ONGOING SUPPORT</h2>
      <p class="faq-body">Our platform was designed to integrate easily into existing production environments. It supports common file formats and can be adapted to specific workflows, reducing the need for major infrastructure changes.</p>
    </div>

    <div class="faq-icon" style="left:109px; top:379px;">
      <svg viewBox="0 0 64 64" fill="none" stroke="#fff" stroke-width="3.5" stroke-linejoin="round" aria-hidden="true">
        <rect x="5" y="10" width="54" height="34" rx="4"/>
        <rect x="12" y="16" width="40" height="22" rx="1"/>
        <path d="M26 44l-4 10h20l-4-10"/>
      </svg>
    </div>
    <div class="faq-text" style="left:225px; top:383px;">
      <h2 class="faq-heading">SOFTWARE COMPATIBILITY</h2>
      <p class="faq-body">After implementation, our team offers comprehensive technical support, including regular updates, performance monitoring, and direct access to engineers and training resources. You're never left on your own.</p>
    </div>

    <div class="faq-icon" style="left:629px; top:379px;">
      <svg viewBox="0 0 64 64" fill="none" stroke="#fff" aria-hidden="true">
        <circle cx="32" cy="32" r="26" stroke-width="5"/>
        <circle cx="32" cy="32" r="9" stroke-width="4"/>
      </svg>
    </div>
    <div class="faq-text" style="left:745px; top:383px;">
      <h2 class="faq-heading">DEMO OR TRIAL OPTIONS</h2>
      <p class="faq-body">Yes — we encourage potential clients to request a personalized demo or pilot program. This helps you evaluate real-world benefits before making a long-term decision.</p>
    </div>

    <h2 class="closing-heading">Still have questions?</h2>
    <p class="closing-note">Reach out to our team — we're happy to help with anything else you need.</p>
  </main>
</body>
</html>
```